VMR business card

Need a business card for a company that provides instructional design and elearning development services. The website is here: http://vantmoro.studio/

I'm attaching a current logo, as well as the old business card design. While I like to keep it clean, the old design is too simplistic for my liking. The only idea I want to reuse from the old design is placing industry jargon on the back of the card, just need a better way to present it. But if you have other ideas for the back--feel free to experiment.

Please use the colors complementary to the color we have on the website. Thank you!

```html
<!DOCTYPE html>
<html lang="en">
<head>
<meta charset="utf-8">
<title>VMR business card</title>
<link rel="stylesheet" href="https://fonts.googleapis.com/css2?family=Arimo:wght@400;700&display=swap">
<style>
  :root{
    --bg:#e9e6e1;
    --card:#f4f4f3;
    --card-shade:#e6e6e5;
    --teal:#2a9d93;
    --teal-dark:#1f8078;
    --gold:#bcae7c;
    --ink:#3a3a3a;
    --grey:#4b4b4b;
  }
  *{margin:0;padding:0;box-sizing:border-box}
  html,body{width:1200px;height:1023px;overflow:hidden;background:var(--bg)}
  body{position:relative;font-family:"Arimo",Arial,sans-serif}
  .card{
    position:absolute;left:180px;width:840px;height:480px;
    background:linear-gradient(135deg,var(--card) 0%,#fbfbfb 45%,var(--card-shade) 100%);
    box-shadow:0 6px 18px rgba(0,0,0,.18);
    overflow:hidden;
  }
  .card--front{top:20px}
  .card--back{top:523px}

  .brand{position:absolute;display:flex;align-items:center;gap:16px}
  .brand__mark{width:44px;height:44px;background:var(--teal)}
  .brand__name{font-weight:700;font-size:50px;color:var(--gold);letter-spacing:-.5px;line-height:1}

  .card--front .brand{left:70px;top:150px}

  .contact{position:absolute;left:480px;top:262px;color:var(--ink)}
  .contact__name{font-size:25px;color:var(--teal);letter-spacing:.5px;margin-bottom:18px;text-transform:uppercase}
  .contact__line{display:flex;align-items:center;gap:8px;font-size:17px;line-height:24px}
  .contact__line svg{width:14px;height:14px;flex:none}

  .edge__rule{position:absolute;left:0;right:0;top:424px;height:3px;background:var(--gold)}
  .edge__band{position:absolute;left:0;right:0;top:436px;bottom:0;background:linear-gradient(180deg,var(--teal),var(--teal-dark))}

  .card--back .brand{left:0;right:0;top:70px;justify-content:center}
  .jargon{position:absolute;left:0;right:0;top:190px;text-align:center;list-style:none;color:var(--grey)}
  .jargon li{font-size:24px;line-height:33px;letter-spacing:.5px;text-transform:uppercase}
</style>
</head>
<body>

<section class="card card--front">
  <div class="brand"><span class="brand__mark"></span><span class="brand__name">Vantmoro Studio</span></div>

  <div class="contact">
    <p class="contact__name">Daniel Korvessky</p>
    <p class="contact__line">
      <svg viewBox="0 0 16 16"><path fill="var(--teal)" d="M3 1l3 3-2 2c1 2 3 4 5 5l2-2 3 3-2 3C6 15 1 10 1 3z"/></svg>
      555-014-2287
    </p>
    <p class="contact__line">
      <svg viewBox="0 0 16 16"><rect x="1" y="3" width="14" height="10" fill="var(--teal)"/><path d="M1 3l7 6 7-6" fill="none" stroke="#fff" stroke-width="1.4"/></svg>
      dkorvessky@vantmoro.studio
    </p>
    <p class="contact__line">
      <svg viewBox="0 0 16 16"><circle cx="8" cy="8" r="7" fill="var(--teal)"/><path d="M1 8h14M8 1c-3 3-3 11 0 14M8 1c3 3 3 11 0 14" fill="none" stroke="#fff" stroke-width="1"/></svg>
      www.vantmoro.studio
    </p>
  </div>

  <div class="edge__rule"></div>
  <div class="edge__band"></div>
</section>

<section class="card card--back">
  <div class="brand"><span class="brand__mark"></span><span class="brand__name">Vantmoro Studio</span></div>
  <ul class="jargon">
    <li>Mobile Learning SCORM</li>
    <li>Instructional Design LMS</li>
    <li>MOOCs eLearning HTML5</li>
    <li>How can we help?</li>
    <li>Adult Learning Theory</li>
    <li>Gamification Classroom</li>
    <li>xAPI Blended Learning</li>
  </ul>
</section>

</body>
</html>
```